Classic/Royal 5 Items Black coloured Stationery Design

Hello,
I'm looking for an Elegant Stationery set consists of 5 items as the following,
1- Letterhead
2- Business Card
3- Invoice
4- CD/DVD with their Envelope Design
5- Envelope
To let the project move ahead easily, I've included a folder consists many designs I liked from various design sites and it consists of,
1- Business card
2- Corporate Identity
3- Invoice
4- Miscellanies
Inside the first three folders, you will find a folder named "Recommended", it contains designs that I like so much and hoping to have a design like them.
The "Miscellanies" folder got some designs for Inspiration.
I'm waiting for some greats designs, a joomla template designer is a bonus for me as I will need him to design the website layer soon.
Due to upload problems at ArtHerdly, I've uploaded the folder in a .rar archive at multiple site and here is the link http://zup.qx/TRALVBNE .
Thank you
Update :- You can use this alternative download link from my Google drive to download the designs
https://files.plomwex.net/file/d/7Kq2ZpR4m8sVxT1nLw9cYb3HfJd5

```html
<!DOCTYPE html>
<html lang="en">
<head>
<meta charset="utf-8">
<title>Velmora — CD Sleeve and Disc</title>
<link rel="stylesheet" href="https://fonts.googleapis.com/css2?family=Libre+Bodoni:wght@700&family=Arimo:wght@400&display=swap">
<style>
  :root {
    --backdrop-light: #e4e4e4;
    --backdrop-dark: #a9a9a9;
    --sleeve-black: #1d1d1d;
    --sleeve-fold: #262626;
    --ink-white: #f2f2f2;
    --disc-white: #fbfbfb;
    --disc-ink: #2a2a2a;
    --hub-grey: #9a9a9a;
    --hub-dark: #5e5e5e;
  }
  html, body {
    margin: 0;
    width: 1200px;
    height: 900px;
    overflow: hidden;
  }
  body {
    position: relative;
    background: radial-gradient(ellipse at 50% 40%, var(--backdrop-light) 0%, var(--backdrop-dark) 100%);
  }
  .sleeve {
    position: absolute;
    left: 120px;
    top: 220px;
    width: 660px;
    height: 460px;
    display: flex;
    box-shadow: 0 18px 30px rgba(0,0,0,0.25);
  }
  .sleeve-panel {
    flex: 1;
    background: var(--sleeve-black);
  }
  .sleeve-panel--back {
    border-right: 1px solid var(--sleeve-fold);
  }
  .sleeve-panel--front {
    display: flex;
    flex-direction: column;
    align-items: center;
    padding-top: 62px;
    box-sizing: border-box;
  }
  .brand-square {
    width: 46px;
    height: 46px;
    border: 2px solid currentColor;
    box-sizing: border-box;
    margin-bottom: 10px;
  }
  .brand-name {
    font-family: "Libre Bodoni", serif;
    font-weight: 700;
    font-size: 30px;
    line-height: 1;
  }
  .brand-tagline {
    font-family: "Arimo", sans-serif;
    font-size: 12px;
    margin-top: 6px;
    letter-spacing: 0.2px;
  }
  .sleeve-panel--front .brand-block { color: var(--ink-white); display: flex; flex-direction: column; align-items: center; }
  .disc {
    position: absolute;
    left: 680px;
    top: 360px;
    width: 440px;
    height: 440px;
    border-radius: 50%;
    background: var(--disc-white);
    box-shadow: 0 14px 30px rgba(0,0,0,0.25);
    color: var(--disc-ink);
  }
  .disc-hub {
    position: absolute;
    left: 140px;
    top: 140px;
  }
  .disc-top {
    position: absolute;
    top: 38px;
    left: 0;
    right: 0;
    display: flex;
    justify-content: center;
  }
  .disc-top .brand-square { width: 40px; height: 40px; }
  .disc-bottom {
    position: absolute;
    top: 325px;
    left: 0;
    right: 0;
    display: flex;
    flex-direction: column;
    align-items: center;
  }
  .disc-bottom .brand-name { font-size: 24px; }
  .disc-bottom .brand-tagline { font-size: 10.5px; }
</style>
</head>
<body>
  <section class="sleeve" aria-label="CD sleeve">
    <div class="sleeve-panel sleeve-panel--back"></div>
    <div class="sleeve-panel sleeve-panel--front">
      <div class="brand-block">
        <div class="brand-square"></div>
        <div class="brand-name">Velmora</div>
        <div class="brand-tagline">Hotels and General Supplies</div>
      </div>
    </div>
  </section>

  <section class="disc" aria-label="CD label">
    <div class="disc-top"><div class="brand-square"></div></div>
    <svg class="disc-hub" width="160" height="160" viewBox="0 0 160 160" aria-hidden="true">
      <circle cx="80" cy="80" r="78" fill="var(--hub-grey)"/>
      <circle cx="80" cy="80" r="62" fill="none" stroke="#d8d8d8" stroke-width="1.5"/>
      <circle cx="80" cy="80" r="46" fill="var(--hub-dark)"/>
      <circle cx="80" cy="80" r="24" fill="var(--backdrop-dark)"/>
    </svg>
    <div class="disc-bottom">
      <div class="brand-name">Velmora</div>
      <div class="brand-tagline">Hotels and General Supplies</div>
    </div>
  </section>
</body>
</html>
```